Prestige Car Bodyshop Business Card

We are a car bodyshop based in the UK. Our customer base is mainly prestige high-value vehicles. I am looking for a classy and stylish business card design for my staff to give out to customers, with their direct email and phone number, as well as our main email and phone number with address details

I am also looking to have a general business card design with just our main company address and contact details, but also have a space to add a manufacturer approval logo (i.e Velmora, Orek, Tovalo etc... logo) in the corner somewhere.

I do not particularly want any outlines or pictures of cars on the card, I would just like a quality high-end look.

Please feel free to get in touch if you have any questions or queries?

Many Thanks

Malcolm

Target Market(s)

Prestige vehicle owners

Industry/Entity Type

Automotive

Contact Information for Business Card

I am looking for a classy and stylish business card design for my staff to give out to customers, with their direct email and phone number, as well as our main email and phone number with address details

Font styles to use
Sans Serif

Colors

Designer to choose colors to be used in the design.

Requirements
Nice to have
• I do not particularly want any outlines or pictures of cars on the card, I would just like a quality high-end look.

```html
<!DOCTYPE html>
<html lang="en">
<head>
<meta charset="utf-8">
<title>RK Halden – Business Cards</title>
<link href="https://fonts.googleapis.com/css2?family=Open+Sans:wght@300;400;600&display=swap" rel="stylesheet">
<style>
  :root{
    --backdrop:#ebe8e3;
    --card-white:#ffffff;
    --navy:#1f4e8c;
    --blue-deep:#164a8f;
    --blue-mid:#1f66b3;
    --blue-light:#3f7fc4;
    --orange:#f28a1e;
    --ink:#2b2b2b;
    --rule:#2d5a96;
    --white:#ffffff;
  }
  *{box-sizing:border-box;margin:0;padding:0}
  html,body{width:1200px;height:1024px;overflow:hidden}
  body{
    background:var(--backdrop);
    font-family:"Open Sans",Arial,sans-serif;
    position:relative;
  }
  .card{
    position:absolute;
    left:190px;
    width:820px;
    height:468px;
    border-radius:34px;
    overflow:hidden;
    box-shadow:0 10px 30px rgba(0,0,0,.18);
  }

  /* Staff card */
  .card--staff{top:30px;background:var(--card-white)}
  .staff__details{
    position:absolute;left:70px;top:64px;width:420px;
  }
  .staff__name{
    font-size:34px;font-weight:400;color:var(--navy);letter-spacing:1px;
  }
  .staff__role{
    font-size:22px;font-weight:400;color:var(--orange);margin-top:2px;
  }
  .staff__address{
    margin-top:40px;font-size:21px;line-height:1.45;color:var(--ink);
  }
  .contact-list{list-style:none;margin-top:22px}
  .contact-list li{
    display:flex;align-items:center;gap:12px;
    font-size:21px;line-height:1.55;color:var(--ink);
  }
  .contact-list svg{width:22px;height:22px;flex:none}
  .staff__divider{
    position:absolute;left:520px;top:40px;width:2px;height:388px;background:var(--rule);
  }
  .staff__emblem{
    position:absolute;left:560px;top:104px;width:260px;height:260px;border-radius:50%;
    background:linear-gradient(135deg,var(--blue-mid),var(--blue-deep) 60%,#4a6a9a);
    display:flex;align-items:center;justify-content:center;
  }
  .staff__emblem span{
    font-size:46px;font-weight:300;color:var(--orange);letter-spacing:2px;
  }

  /* Company card */
  .card--company{
    top:526px;
    background:linear-gradient(160deg,var(--blue-deep) 0%,var(--blue-mid) 45%,var(--blue-light) 100%);
  }
  .brand{
    position:absolute;left:330px;top:120px;width:420px;color:var(--white);
  }
  .brand__name{
    font-size:64px;font-weight:300;letter-spacing:3px;line-height:1;
  }
  .brand__tagline{
    font-size:19px;font-weight:400;letter-spacing:2px;margin-top:14px;
    padding-bottom:10px;border-bottom:2px solid var(--white);
  }
  .brand__web{font-size:18px;margin-top:10px;letter-spacing:1px}
  .approvals{
    position:absolute;left:60px;bottom:56px;display:flex;gap:40px;align-items:center;
  }
  .approvals span{
    font-size:22px;font-weight:400;color:var(--white);letter-spacing:2px;
  }
</style>
</head>
<body>

<section class="card card--staff" aria-label="Staff business card">
  <div class="staff__details">
    <h1 class="staff__name">DANIEL REEVE</h1>
    <p class="staff__role">Company Employee</p>
    <address class="staff__address" style="font-style:normal">
      Eastfield Road,<br>Mill Common<br>Harlow Vale, Bristol BS40 2QT
    </address>
    <ul class="contact-list">
      <li>
        <svg viewBox="0 0 22 22"><circle cx="11" cy="11" r="11" fill="var(--navy)"/><path d="M7.5 6h2l1 3-1.3 1a6 6 0 0 0 2.8 2.8l1-1.3 3 1v2a1 1 0 0 1-1 1A9 9 0 0 1 6.5 7a1 1 0 0 1 1-1z" fill="#fff"/></svg>
        0117 000 4821
      </li>
      <li>
        <svg viewBox="0 0 22 22"><circle cx="11" cy="11" r="11" fill="var(--navy)"/><path d="M7.5 6h2l1 3-1.3 1a6 6 0 0 0 2.8 2.8l1-1.3 3 1v2a1 1 0 0 1-1 1A9 9 0 0 1 6.5 7a1 1 0 0 1 1-1z" fill="#fff"/></svg>
        0117 000 5937
      </li>
      <li>
        <svg viewBox="0 0 22 22"><circle cx="11" cy="11" r="11" fill="var(--navy)"/><rect x="5.5" y="7.5" width="11" height="7.5" fill="#fff"/><path d="M5.5 7.5 11 12l5.5-4.5" fill="none" stroke="var(--navy)" stroke-width="1.2"/></svg>
        info@rkhalden.co.uk
      </li>
      <li>
        <svg viewBox="0 0 22 22"><circle cx="11" cy="11" r="11" fill="var(--navy)"/><circle cx="11" cy="11" r="5.5" fill="none" stroke="#fff" stroke-width="1.3"/><path d="M5.5 11h11M11 5.5c-2.5 3-2.5 8 0 11M11 5.5c2.5 3 2.5 8 0 11" fill="none" stroke="#fff" stroke-width="1.1"/></svg>
        www.rkhalden.co.uk
      </li>
    </ul>
  </div>
  <div class="staff__divider"></div>
  <div class="staff__emblem"><span>HALDEN</span></div>
</section>

<section class="card card--company" aria-label="Company business card">
  <div class="brand">
    <p class="brand__name">RK HALDEN</p>
    <p class="brand__tagline">ACCIDENT REPAIR CENTRE</p>
    <p class="brand__web">www.rkhalden.co.uk</p>
  </div>
  <div class="approvals" aria-label="Manufacturer approvals">
    <span>VELMORA</span>
    <span>OREK</span>
    <span>TOVALO</span>
  </div>
</section>

</body>
</html>
```